vireo nuts company small package

we are looking to design a package for our nuts 10cm by 13 cm and also 3.25 inch by 4.5 inches. our nuts are:
Salted peanuts
honey roasted peanuts
salted cashews
honey roasted cashews
pistachios
sunflower seeds

have a floral design simple yet elegant not too crowded
our product is non GMO

some of our competitors:
http://kestrabite.example/
http://www.dovuhusk.example/sg/
http://tirotiro.example/en/content/view/5/17/

Target Market(s)

european market, Middle eastern market

Industry/Entity Type

It Company

Font styles to use
Decorative
Script

Requirements
Must have
• floral design not crowded yet elegant
• high resolution pictures of the nuts
Nice to have
Should not have
• cartoon characters

```html
<!DOCTYPE html>
<html lang="en">
<head>
<meta charset="utf-8">
<title>Vireo Nuts – Package Designs</title>
<link href="https://fonts.googleapis.com/css2?family=Oswald:wght@400;500;700&display=swap" rel="stylesheet">
<style>
  :root {
    --stage: #2b2b2b;
    --pack-dark: #141414;
    --pattern-mid: #262626;
    --gold-deep: #b8962e;
    --gold-mid: #d4b24c;
    --gold-light: #f6e9ae;
    --silver-deep: #bdbdbd;
    --silver-mid: #d6d6d6;
    --silver-light: #fbfbfb;
    --ink: #2f2f2f;
    --white: #ffffff;
    --honey-dark: #a8661f;
    --honey-light: #dc9c4c;
    --salt-dark: #c4843a;
    --salt-light: #ecbd78;
  }
  * { box-sizing: border-box; margin: 0; padding: 0; }
  html, body {
    width: 1200px; height: 1120px; overflow: hidden;
    background: var(--stage);
    font-family: "Oswald", "Arial Narrow", sans-serif;
  }
  .package {
    position: absolute; top: 108px; width: 521px; height: 679px;
    background: var(--pack-dark);
    overflow: hidden;
  }
  .package--honey { left: 47px; }
  .package--salted { left: 639px; }

  .package__crown {
    position: absolute; left: 0; top: 0; width: 100%; height: 282px;
    background: radial-gradient(ellipse at 50% 45%, var(--pattern-mid), var(--pack-dark) 75%);
  }
  .package--honey .package__crown { border-top: 3px solid var(--gold-mid); }
  .package--salted .package__crown { border-top: 3px solid var(--gold-mid); }

  .brand {
    position: absolute; left: 0; top: 0; width: 100%; height: 282px;
    display: flex; align-items: center; justify-content: center;
  }
  .brand__name {
    font-weight: 500; font-size: 74px; letter-spacing: 1px;
    color: var(--white); line-height: 1;
  }

  .flavour-band {
    position: absolute; left: 0; top: 282px; width: 100%; height: 122px;
    display: flex; align-items: center; justify-content: center;
  }
  .flavour-band::before, .flavour-band::after {
    content: ""; position: absolute; left: 0; width: 100%; height: 2px;
    background: rgba(255,255,255,0.55);
  }
  .flavour-band::before { top: 8px; }
  .flavour-band::after { bottom: 6px; }
  .flavour-band__title {
    font-weight: 400; font-size: 47px; color: var(--ink);
    letter-spacing: 0.2px; line-height: 1;
  }

  .nut-photo {
    position: absolute; left: 0; top: 404px; width: 100%; height: 228px;
  }
  .package--honey .nut-photo {
    background: radial-gradient(ellipse at 50% 50%, var(--honey-light), var(--honey-dark));
  }
  .package--salted .nut-photo {
    background: radial-gradient(ellipse at 50% 50%, var(--salt-light), var(--salt-dark));
  }

  .info-band {
    position: absolute; left: 0; top: 632px; width: 100%; height: 47px;
    display: flex; align-items: center; justify-content: space-between;
    padding: 0 40px 0 22px;
    font-weight: 400; font-size: 18px; color: var(--ink);
  }

  .package--honey .flavour-band,
  .package--honey .info-band {
    background: linear-gradient(90deg, var(--gold-deep), var(--gold-light) 28%, var(--gold-mid) 55%, var(--gold-light) 82%, var(--gold-deep));
  }
  .package--salted .flavour-band,
  .package--salted .info-band {
    background: linear-gradient(90deg, var(--silver-deep), var(--silver-light) 28%, var(--silver-mid) 55%, var(--silver-light) 82%, var(--silver-deep));
  }
</style>
</head>
<body>

  <section class="package package--honey">
    <div class="package__crown" role="img" aria-label="Black damask floral pattern background"></div>
    <div class="brand"><span class="brand__name">VIREO</span></div>
    <div class="flavour-band"><h2 class="flavour-band__title">HONEY ROASTED PEANUTS</h2></div>
    <div class="nut-photo" role="img" aria-label="Photograph of honey roasted peanuts"></div>
    <div class="info-band"><span class="info-band__claim">non GMO</span><span class="info-band__content">Cont:</span></div>
  </section>

  <section class="package package--salted">
    <div class="package__crown" role="img" aria-label="Black damask floral pattern background"></div>
    <div class="brand"><span class="brand__name">VIREO</span></div>
    <div class="flavour-band"><h2 class="flavour-band__title">SALTED PEANUTS</h2></div>
    <div class="nut-photo" role="img" aria-label="Photograph of salted peanuts"></div>
    <div class="info-band"><span class="info-band__claim">non GMO</span><span class="info-band__content">Cont:</span></div>
  </section>

</body>
</html>
```